Environmental law firm Biz cards and stationery
Law Offices of Wendell T. Haverbrook, P.C.
Simple
Wendell T. Haverbrook
742 Dunmore Boulevard
Suite 312
Glenmora, Illinois 60099
847-555-0193 x 14
wth@haverbrooklegal.example
www.haverbrooklegal.example
I wish to use the logo that appears on my website, except for the color, which I prefer to be either black or navy blue. However, I am not opposed to using the variant of the logo showing the tree centered on top, rather than to the side. It depends on the overall appearance. Also, for the stationery letterhead, I prefer to have all contact information at the top of the page, rather than on the bottom. And, because new personnel may be added to the firm, please anticipate that the writer's fax and e-mail address will be added separately and thus not printed. Thank you.
I am uploading 2 files, containing variants of the logo I selected. One is oriented vertically, the other horizontally. Also, one has a shadow effect; the other does not.

```html
<!DOCTYPE html>
<html lang="en">
<head>
<meta charset="utf-8">
<title>Wendell T. Haverbrook, P.C. — Business Cards</title>
<link rel="stylesheet" href="https://fonts.googleapis.com/css2?family=Cinzel:wght@400;500&display=swap">
<style>
  :root {
    --navy: #1b2a4e;
    --navy-deep: #121d38;
    --paper: #f4f4f2;
    --paper-shade: #e4e5e6;
    --ink: #2a3350;
    --rule: #7d869c;
    --pale: #c9cfdc;
    --backdrop: #d9dadc;
  }
  * { margin: 0; padding: 0; box-sizing: border-box; }
  html, body {
    width: 1200px; height: 901px; overflow: hidden;
    background: var(--backdrop);
    font-family: "Cinzel", "Times New Roman", serif;
    color: var(--ink);
  }
  .canvas { position: relative; width: 1200px; height: 901px; }

  .card {
    position: absolute; width: 560px; height: 320px;
    box-shadow: 0 6px 18px rgba(0,0,0,0.22);
    overflow: hidden;
  }

  /* Back of card */
  .card-back {
    left: 50px; top: 110px;
    background: linear-gradient(135deg, var(--navy) 0%, var(--navy-deep) 100%);
    color: var(--pale);
    display: flex; flex-direction: column; align-items: center; justify-content: center;
  }
  .back-mark {
    width: 150px; height: 150px;
    border: 3px solid var(--pale);
    padding: 6px;
  }
  .back-mark span {
    display: block; width: 100%; height: 100%;
    background: linear-gradient(180deg, var(--pale) 0%, #aeb7c9 100%);
  }
  .back-web { margin-top: 34px; font-size: 13px; letter-spacing: 4px; text-transform: uppercase; }

  /* Front of card */
  .card-front {
    left: 590px; top: 470px;
    background: linear-gradient(160deg, #ffffff 0%, var(--paper) 55%, var(--paper-shade) 100%);
  }
  .brand {
    position: absolute; left: 150px; top: 30px;
    display: flex; align-items: center; gap: 12px;
  }
  .brand-square { width: 40px; height: 40px; background: var(--navy); }
  .brand-name { font-size: 17px; line-height: 1.25; color: var(--navy); }
  .brand-name .lead {
    display: block; font-size: 13px; letter-spacing: 1px;
    border-bottom: 1px solid var(--navy); padding-bottom: 2px; margin-bottom: 3px;
  }

  .person {
    position: absolute; left: 34px; top: 128px;
    font-size: 18px; letter-spacing: 0.5px; color: var(--ink);
  }
  .divider {
    position: absolute; left: 300px; top: 110px; width: 1px; height: 120px;
    background: var(--rule);
  }
  .contact {
    position: absolute; left: 314px; top: 108px;
    font-size: 11.5px; line-height: 15px; color: var(--ink); list-style: none;
  }
  .contact .address { margin-bottom: 4px; }
  .contact li { display: flex; align-items: center; gap: 7px; }
  .contact svg { width: 11px; height: 11px; fill: var(--ink); flex: none; }
  .contact .email { text-transform: uppercase; }

  .band-rule {
    position: absolute; left: 0; right: 0; bottom: 56px; height: 2px; background: var(--navy);
  }
  .band {
    position: absolute; left: 0; right: 0; bottom: 0; height: 48px;
    background: var(--navy);
    color: var(--pale);
    display: flex; align-items: center; justify-content: center;
    font-size: 13px; letter-spacing: 4px; text-transform: uppercase;
  }
</style>
</head>
<body>
<main class="canvas">

  <section class="card card-back">
    <div class="back-mark"><span role="img" aria-label="Framed tree emblem of the firm"></span></div>
    <p class="back-web">www.haverbrooklegal.example</p>
  </section>

  <section class="card card-front">
    <header class="brand">
      <div class="brand-square"></div>
      <p class="brand-name"><span class="lead">Law Offices of</span>Wendell T. Haverbrook, P.C.</p>
    </header>

    <p class="person">Wendell T. Haverbrook</p>
    <div class="divider"></div>

    <ul class="contact">
      <li class="address">742 Dunmore Boulevard<br>Suite 312<br>Glenmora, Illinois 60099</li>
      <li>
        <svg viewBox="0 0 12 12" aria-hidden="true"><path d="M2 1h3l1 3-1.5 1a7 7 0 0 0 2.5 2.5L8 6l3 1v3a1 1 0 0 1-1 1A9 9 0 0 1 1 2a1 1 0 0 1 1-1z"/></svg>
        847-555-0193 x 14
      </li>
      <li>
        <svg viewBox="0 0 12 12" aria-hidden="true"><rect x="3" y="1" width="6" height="4"/><rect x="1" y="5" width="10" height="6" rx="1"/></svg>
        312-555-0148
      </li>
      <li>
        <svg viewBox="0 0 12 12" aria-hidden="true"><rect x="3" y="0.5" width="6" height="11" rx="1"/><rect x="4" y="2" width="4" height="6" fill="#f4f4f2"/></svg>
        312-555-0172
      </li>
      <li class="email">
        <svg viewBox="0 0 12 12" aria-hidden="true"><rect x="0.5" y="2.5" width="11" height="7"/><path d="M0.5 2.5 6 7l5.5-4.5" fill="none" stroke="#f4f4f2" stroke-width="1"/></svg>
        wth@haverbrooklegal.example
      </li>
    </ul>

    <div class="band-rule"></div>
    <footer class="band">www.haverbrooklegal.example</footer>
  </section>

</main>
</body>
</html>
```